Data analytics company needs a website banner design

We need an image for our website's slider. Our website uses the Tessara template from PixVault (https://pixvault.example/site-theme/tessara/). We are a data analytics company that develops real-time process monitoring software for manufacturing. Our initial product, FlowSense, relies upon AI and machine learning algorithms to provide fault and anomaly detection for manufacturing process health. We would like to see designs that (a) incorporate some of the following concepts, AI, pattern recognition, digital transformation (1s and 0s), machine learning, health, etc., and (b) illustrate a screenshot of our software superimposed on a large desktop flat screen monitor. The focus should be on the screenshot on the monitor, while the other concepts (1s and 0s etc) should be subtle (potentially fading out from left to right) with the monitor on the right. It would be nice if I could swap out the screenshot once the design is complete. An example screenshot is provided in the Upload Files. Different resolutions and ratios of the screenshot can be generated if necessary.
Look and feel
Each slider illustrates characteristics of the customer's brand and the style your logo design should communicate.

```html
<!DOCTYPE html>
<html lang="en">
<head>
<meta charset="utf-8">
<title>FlowSense – Manufacturing Behavioral Analysis</title>
<link rel="stylesheet" href="https://fonts.googleapis.com/css2?family=Quicksand:wght@400;600&family=Inter:wght@400;600&display=swap">
<style>
  :root{
    --bg-deep:#24126e;
    --bg-mid:#3a1c9a;
    --bg-violet:#6a2fc4;
    --head-cyan:#9fe9f2;
    --head-lilac:#b68cf0;
    --white:#ffffff;
    --bezel:#2b2b2f;
    --chin:#ececf0;
    --chin-edge:#c9c9d2;
    --stand:#dcdce2;
    --stand-shadow:#1b0d50;
    --ui-bg:#f1f1f3;
    --ui-bar:#dcdce3;
    --ui-line:#b9b9c4;
    --ui-text:#2d2d35;
    --ui-select:#9fc06a;
    --plot-blue:#2c3fd6;
    --plot-red:#e2483c;
    --plot-green:#63c45b;
    --plot-fill:#d8f5cf;
    --plot-noise:#a4a4ab;
  }
  *{margin:0;padding:0;box-sizing:border-box}
  html,body{width:1200px;height:578px;overflow:hidden;background:var(--bg-deep)}
  .banner{
    position:relative;width:1200px;height:578px;overflow:hidden;
    background:
      radial-gradient(ellipse 520px 380px at 900px 330px, rgba(80,40,180,.45), transparent 70%),
      linear-gradient(100deg,var(--bg-violet) 0%,var(--bg-mid) 38%,var(--bg-deep) 100%);
  }
  .binary-field{
    position:absolute;inset:0;
    background:linear-gradient(90deg, rgba(138,91,224,.38) 0%, rgba(138,91,224,.18) 45%, rgba(138,91,224,.06) 100%);
  }
  .head-art{
    position:absolute;left:169px;top:62px;width:400px;height:516px;
    border-radius:48% 52% 30% 40% / 40% 45% 20% 20%;
    background:
      radial-gradient(ellipse 60% 55% at 55% 40%, rgba(159,233,242,.35), transparent 75%),
      linear-gradient(160deg, rgba(159,233,242,.28) 0%, rgba(182,140,240,.25) 60%, rgba(182,140,240,.05) 100%);
  }
  .brand{position:absolute;left:858px;top:42px;display:flex;align-items:center;gap:12px}
  .brand-dot{width:66px;height:66px;border:2px solid var(--white);border-radius:50%}
  .brand-text{padding-top:10px}
  .brand-name{
    font-family:"Quicksand",sans-serif;font-weight:400;font-size:33px;line-height:1;
    color:var(--white);letter-spacing:1.5px;
  }
  .brand-tagline{
    font-family:"Quicksand",sans-serif;font-weight:600;font-size:8.2px;
    color:var(--white);letter-spacing:1.9px;margin-top:9px;white-space:nowrap;
  }
  .monitor{position:absolute;left:679px;top:153px;width:460px;height:420px}
  .monitor-shadow{
    position:absolute;left:-1px;top:345px;width:478px;height:67px;border-radius:50%;
    background:radial-gradient(ellipse at center, var(--stand-shadow) 0%, rgba(27,13,80,.75) 60%, transparent 100%);
  }
  .monitor-stand{
    position:absolute;left:148px;top:306px;width:89px;height:66px;
    background:linear-gradient(90deg,var(--chin-edge),var(--stand) 50%,var(--chin-edge));
  }
  .monitor-body{
    position:absolute;left:0;top:0;width:460px;height:310px;border-radius:9px;
    background:var(--bezel);overflow:hidden;
  }
  .monitor-chin{
    position:absolute;left:0;bottom:0;width:100%;height:65px;
    background:linear-gradient(180deg,var(--chin),var(--chin-edge));
  }
  .monitor-screen{position:absolute;left:14px;top:13px;width:430px;height:232px;background:var(--ui-bg);overflow:hidden}
  .monitor-screen svg{display:block}
  .ui-text{font-family:"Inter",sans-serif;fill:var(--ui-text)}
</style>
</head>
<body>
<main class="banner">
  <div class="binary-field" role="img" aria-label="Subtle grid of glowing binary digits 1 and 0 fading from left to right"></div>
  <div class="head-art" role="img" aria-label="Line-art illustration of a human head in profile formed by maze-like circuit lines"></div>

  <header class="brand">
    <span class="brand-dot"></span>
    <div class="brand-text">
      <div class="brand-name">FlowSense</div>
      <div class="brand-tagline">MANUFACTURING BEHAVIORAL ANALYSIS</div>
    </div>
  </header>

  <section class="monitor" aria-label="Desktop monitor showing FlowSense software">
    <div class="monitor-shadow"></div>
    <div class="monitor-stand"></div>
    <div class="monitor-body">
      <div class="monitor-chin"></div>
      <div class="monitor-screen">
        <svg width="430" height="232" viewBox="0 0 430 232">
          <defs>
            <symbol id="signal-panel" viewBox="0 0 166 107">
              <rect width="166" height="107" fill="#fff" stroke="var(--ui-line)" stroke-width=".5"/>
              <rect width="166" height="8" fill="var(--ui-bar)"/>
              <text class="ui-text" x="3" y="6" font-size="4.6">Signal View</text>
              <rect x="14" y="19" width="147" height="76" fill="#fff" stroke="#555" stroke-width=".5"/>
              <path d="M18,40 C30,30 40,50 52,38 S74,30 86,42 S108,52 120,36 S142,32 157,44"
                fill="none" stroke="var(--plot-noise)" stroke-width="4" opacity=".45"/>
              <path d="M16,90 L22,90 L26,42 C40,36 52,46 66,40 S92,36 104,48 L110,70 L116,46 C130,38 142,44 152,40 L156,90"
                fill="none" stroke="var(--plot-blue)" stroke-width="1"/>
              <rect x="116" y="21" width="42" height="8" fill="#fff" stroke="#777" stroke-width=".4"/>
              <text class="ui-text" x="119" y="27" font-size="4.2">Sensor: Mean</text>
              <text class="ui-text" x="76" y="103" font-size="4.2">Time, [s]</text>
            </symbol>
            <symbol id="compare-panel" viewBox="0 0 166 107">
              <rect width="166" height="107" fill="#fff" stroke="var(--ui-line)" stroke-width=".5"/>
              <rect width="166" height="8" fill="var(--ui-bar)"/>
              <text class="ui-text" x="3" y="6" font-size="4.6">Compare View</text>
              <text class="ui-text" x="14" y="15.5" font-size="5.2" font-weight="600">Baseline Deviation Overview</text>
              <rect x="14" y="19" width="147" height="76" fill="#fff" stroke="#555" stroke-width=".5"/>
              <path d="M16,50 H48 V46 H80 V60 H112 V52 H158 V40 H112 V44 H80 V38 H48 V42 H16 Z" fill="var(--plot-fill)"/>
              <path d="M16,42 H48 V38 H80 V44 H112 V40 H158" fill="none" stroke="var(--plot-green)" stroke-width=".8"/>
              <path d="M16,50 H48 V46 H80 V60 H112 V52 H158" fill="none" stroke="var(--plot-red)" stroke-width=".8"/>
              <g stroke="var(--plot-blue)" stroke-width="1.2">
                <line x1="24" y1="46" x2="40" y2="46"/><line x1="56" y1="42" x2="72" y2="42"/>
                <line x1="88" y1="52" x2="104" y2="52"/><line x1="124" y1="46" x2="146" y2="46"/>
              </g>
              <text class="ui-text" x="76" y="103" font-size="4.2">Time, [s]</text>
            </symbol>
          </defs>

          <rect x="0" y="0" width="430" height="15" fill="var(--ui-bar)"/>
          <g fill="#7a86a8">
            <rect x="4" y="4" width="7" height="7"/><rect x="14" y="4" width="7" height="7"/>
            <rect x="24" y="4" width="7" height="7"/><rect x="34" y="4" width="7" height="7"/>
          </g>
          <g fill="none" stroke="#4a5570" stroke-width="1">
            <circle cx="52" cy="7" r="3"/><circle cx="62" cy="7" r="3"/><circle cx="72" cy="7" r="3"/>
          </g>
          <rect x="360" y="3" width="66" height="9" fill="#fff" stroke="var(--ui-line)" stroke-width=".5"/>
          <text class="ui-text" x="364" y="9.6" font-size="4.8" fill="#888">Search</text>

          <g class="ui-tree">
            <rect x="0" y="15" width="95" height="217" fill="#fff" stroke="var(--ui-line)" stroke-width=".5"/>
            <rect x="0" y="15" width="95" height="8" fill="var(--ui-bar)"/>
            <text class="ui-text" x="3" y="21" font-size="4.6">Workspace</text>
            <g font-size="4.3" class="ui-text">
              <text x="6" y="30">Plant Overview</text>
              <text x="11" y="37">Lines</text>
              <text x="16" y="44">Line North</text>
              <text x="22" y="51">Sensors</text>
              <text x="22" y="58">Reports</text>
              <text x="22" y="65">Models</text>
              <text x="28" y="72">Baselines</text>
              <text x="28" y="79">Alerts</text>
              <text x="16" y="86">Line South</text>
              <text x="22" y="93">Sensors</text>
              <text x="22" y="100">Reports</text>
              <text x="22" y="107">Models</text>
              <rect x="24" y="110" width="71" height="6" fill="var(--ui-select)"/>
              <text x="28" y="114.6">Baselines</text>
              <text x="28" y="121">Alerts</text>
              <text x="11" y="128">Archive</text>
              <text x="6" y="135">Settings</text>
            </g>
            <rect x="0" y="223" width="95" height="9" fill="var(--ui-bar)"/>
            <text class="ui-text" x="3" y="229.5" font-size="4.6">Status</text>
          </g>

          <use href="#signal-panel" x="97" y="15" width="166" height="107"/>
          <text class="ui-text" x="101" y="30.5" font-size="5.2" font-weight="600">Health Monitor: Line North</text>
          <use href="#compare-panel" x="264" y="15" width="166" height="107"/>

          <use href="#signal-panel" x="97" y="124" width="166" height="107"/>
          <text class="ui-text" x="101" y="139.5" font-size="5.2" font-weight="600">Health Monitor: Line South</text>
          <use href="#compare-panel" x="264" y="124" width="166" height="107"/>
        </svg>
      </div>
    </div>
  </section>
</main>
</body>
</html>
```